Sleek, Professional Business Card Design Needed

Business Cards - Logo Attached.

We are a solar consulting company. We are national and want our cards to represent the professional high quality products that we offer.

Industry/Entity Type

Business

Contact Information for Business Card

n/a

Requirements
Must have
• Design
• Name
• Position
• Number
• Email
• Address
Should not have
• Not be too crowded

```html
<!DOCTYPE html>
<html lang="en">
<head>
<meta charset="utf-8">
<title>Solvane Energy – Business Card</title>
<link rel="stylesheet" href="https://fonts.googleapis.com/css2?family=Arimo:wght@400;700&display=swap">
<style>
  :root {
    --page: #ffffff;
    --card: #393939;
    --text-light: #d9d9d9;
    --text-soft: #c4c4c4;
    --rule: #8a8a8a;
    --brand-blue: #1a8fcd;
    --brand-green: #8dc63f;
  }
  * { margin: 0; padding: 0; box-sizing: border-box; }
  html, body {
    width: 1200px;
    height: 1200px;
    overflow: hidden;
    background: var(--page);
  }
  .canvas {
    position: relative;
    width: 1200px;
    height: 1200px;
    font-family: "Arimo", Arial, sans-serif;
  }
  .card {
    position: absolute;
    left: 403px;
    top: 299px;
    width: 394px;
    height: 630px;
    background: var(--card);
    color: var(--text-light);
    text-align: center;
  }
  .brand-mark {
    position: absolute;
    left: 50%;
    top: 76px;
    width: 92px;
    height: 92px;
    margin-left: -46px;
    border-radius: 50%;
    border: 5px solid var(--brand-blue);
  }
  .brand-name {
    position: absolute;
    left: 0;
    right: 0;
    top: 172px;
    font-weight: 700;
    font-size: 25px;
    letter-spacing: 0.5px;
    color: var(--brand-green);
  }
  .person-name {
    position: absolute;
    left: 0; right: 0;
    top: 287px;
    font-size: 29px;
    font-weight: 400;
    letter-spacing: 0.5px;
    color: var(--text-soft);
  }
  .person-position {
    position: absolute;
    left: 0; right: 0;
    top: 340px;
    font-size: 13px;
    font-weight: 700;
    letter-spacing: 9px;
    padding-left: 9px;
    color: var(--text-light);
  }
  .divider {
    position: absolute;
    left: 50%;
    top: 393px;
    width: 53px;
    margin-left: -26px;
    border-top: 1px solid var(--rule);
  }
  .contact {
    position: absolute;
    left: 0; right: 0;
    color: var(--text-light);
  }
  .contact-phone { top: 430px; font-size: 19px; letter-spacing: 3px; }
  .contact-email { top: 468px; font-size: 15px; letter-spacing: 1.2px; }
  .contact-street { top: 501px; font-size: 15px; letter-spacing: 0.3px; }
  .contact-city { top: 536px; font-size: 11px; letter-spacing: 0.8px; }
</style>
</head>
<body>
<div class="canvas">
  <section class="card">
    <div class="brand-mark"></div>
    <div class="brand-name">SOLVANE ENERGY</div>

    <h1 class="person-name">Your Name Here</h1>
    <div class="person-position">POSITION</div>
    <div class="divider"></div>

    <div class="contact contact-phone">012 345 678</div>
    <div class="contact contact-email">youremail@mail.com</div>
    <div class="contact contact-street">321 Energy Road, Energy</div>
    <div class="contact contact-city">YOUR CITY, YOUR COUNTRY</div>
  </section>
</div>
</body>
</html>
```